Home inspection business! professional look attracting customers just by looks. Read must haves

its a new business I started on my own for home inspections I would like something very professional to give to real estate agents and clients, its going to have my license number on it my business phone number my name my website as well etc on the back side it will be servicing areas and also what kind of services I offer I also have a business card from someone else the way I would like mine to be. I will attach my logo

Home Inspection

listed in nice to haves

• phone number - 555 293 8471
• website- hollowpinecheck.com
• license number #2938475610
• my name Gavin keropulis
• picture of my logo and me on the front
• on the back of the card. stating I am servicing All of New York and Long Island
• also services I will offer will be home inspection -mold inspection -lead inspection -radon inspection -Termite Inspection -Infared Scan.
• and also we provide inspections for single family homes condos co-ops town-homes
• and commercial property
• same colors as the logos and also if you recommend fonts to look like the logo not sure up to you

```html
<!DOCTYPE html>
<html lang="en">
<head>
<meta charset="utf-8">
<title>Hollow Pine Check – Business Card</title>
<link href="https://fonts.googleapis.com/css2?family=Montserrat:wght@500;600&family=Ubuntu:wght@300;400;500&display=swap" rel="stylesheet">
<style>
  :root {
    --backdrop: #e9e6e1;
    --card: #25282c;
    --card-deep: #1f2225;
    --blue: #5b9bd5;
    --grey: #8a8d91;
    --grey-band: #6f7276;
    --light: #f2f2f2;
    --muted: #9a9da1;
  }
  * { margin: 0; padding: 0; box-sizing: border-box; }
  html, body { width: 1200px; height: 859px; overflow: hidden; }
  body {
    background: var(--backdrop);
    font-family: "Ubuntu", Arial, sans-serif;
    position: relative;
  }
  .card {
    position: absolute;
    top: 289px;
    width: 500px;
    height: 285px;
    background: linear-gradient(135deg, var(--card) 0%, var(--card-deep) 100%);
    overflow: hidden;
    box-shadow: 0 10px 24px rgba(0,0,0,.25);
  }
  .card-front { left: 61px; border-left: 2px solid var(--blue); }
  .card-back { left: 639px; border-right: 2px solid var(--blue); }
  .card-stripes { position: absolute; inset: 0; }

  .brand {
    position: absolute;
    display: flex;
    align-items: center;
    gap: 8px;
    font-family: "Montserrat", Arial, sans-serif;
    font-weight: 600;
    letter-spacing: .5px;
    text-transform: uppercase;
  }
  .brand-dot { border-radius: 50%; flex: none; }
  .card-front .brand { left: 20px; top: 48px; font-size: 17px; color: var(--grey); }
  .card-front .brand-dot { width: 26px; height: 26px; border: 4px solid var(--grey); }

  .holder-name {
    position: absolute; left: 23px; top: 136px;
    font-family: "Montserrat", Arial, sans-serif;
    font-weight: 600; font-size: 17px; color: var(--blue);
    text-transform: uppercase; letter-spacing: -.2px;
  }
  .holder-role {
    position: absolute; left: 23px; top: 157px;
    font-size: 12.5px; font-weight: 300; color: var(--muted);
  }
  .holder-rule {
    position: absolute; left: 23px; top: 180px;
    width: 200px; height: 1px; background: #55585c;
  }
  .contact-list { position: absolute; left: 23px; top: 192px; list-style: none; }
  .contact-list li {
    display: flex; align-items: center; gap: 6px;
    height: 17.5px; font-size: 12.5px; font-weight: 300; color: var(--muted);
  }
  .contact-list svg { width: 12px; height: 12px; flex: none; }
  .accent { color: var(--blue); font-weight: 400; }
  .license {
    position: absolute; left: 23px; top: 253px;
    font-size: 12.5px; font-weight: 300; color: var(--muted);
  }
  .license .accent { font-weight: 500; }

  .card-back .brand {
    left: 0; right: 0; top: 80px; justify-content: center;
    font-size: 22px; color: var(--light);
  }
  .card-back .brand-dot { width: 30px; height: 30px; border: 5px solid var(--light); }
  .service-area {
    position: absolute; left: 0; right: 0; top: 146px; text-align: center;
    font-family: "Montserrat", Arial, sans-serif; font-weight: 600;
    font-size: 12.5px; letter-spacing: .6px; color: var(--blue);
  }
  .service-rule {
    position: absolute; left: 29px; width: 442px; top: 175px;
    height: 1.5px; background: var(--blue);
  }
  .service-list {
    position: absolute; left: 0; right: 0; top: 188px; text-align: center;
    font-size: 12.5px; line-height: 17.5px; color: var(--light); font-weight: 300;
  }
  .service-list .sep { color: var(--blue); padding: 0 2px; }
  .property-types {
    position: absolute; left: 20px; right: 20px; top: 236px; text-align: center;
    font-size: 12.5px; line-height: 17.5px; color: var(--light); font-weight: 300;
  }
</style>
</head>
<body>

<section class="card card-front">
  <svg class="card-stripes" viewBox="0 0 500 285" aria-hidden="true">
    <polygon points="285,285 433,285 500,218 500,70" fill="#5b9bd5"/>
    <polygon points="436,285 500,285 500,222" fill="#6f7276"/>
  </svg>

  <div class="brand"><span class="brand-dot"></span>Hollow Pine Check</div>

  <h1 class="holder-name">Gavin Keropulis</h1>
  <p class="holder-role">Training Specialist</p>
  <div class="holder-rule"></div>

  <ul class="contact-list">
    <li>
      <svg viewBox="0 0 12 12" aria-hidden="true"><circle cx="6" cy="6" r="5.2" fill="none" stroke="#5b9bd5" stroke-width="1"/><path d="M4 3.4l1 1.2-.6.7c.4.8 1 1.4 1.8 1.8l.7-.6 1.2 1-.6.9c-1.8-.2-3.6-2-3.8-3.8z" fill="#5b9bd5"/></svg>
      555 293 8471
    </li>
    <li>
      <svg viewBox="0 0 12 12" aria-hidden="true"><rect x="1" y="2.5" width="10" height="7" fill="none" stroke="#5b9bd5" stroke-width="1"/><path d="M1 2.5l5 4 5-4" fill="none" stroke="#5b9bd5" stroke-width="1"/></svg>
      gavin@hollowpinecheck.com
    </li>
    <li>
      <svg viewBox="0 0 12 12" aria-hidden="true"><circle cx="6" cy="6" r="5" fill="none" stroke="#5b9bd5" stroke-width="1"/><ellipse cx="6" cy="6" rx="2.2" ry="5" fill="none" stroke="#5b9bd5" stroke-width="1"/><path d="M1 6h10M2 3.5h8M2 8.5h8" stroke="#5b9bd5" stroke-width=".8"/></svg>
      www.<span class="accent">hollowpinecheck</span>.com
    </li>
  </ul>

  <p class="license">License Number <span class="accent">#2938475610</span></p>
</section>

<section class="card card-back">
  <svg class="card-stripes" viewBox="0 0 500 285" aria-hidden="true">
    <polygon points="68,0 145,0 0,145 0,70" fill="#5b9bd5"/>
  </svg>

  <div class="brand"><span class="brand-dot"></span>Hollow Pine Check</div>

  <p class="service-area">I AM SERVICING ALL OF NEW YORK AND LONG ISLAND</p>
  <div class="service-rule"></div>

  <p class="service-list">
    Home inspection<span class="sep">|</span>Mold inspection<span class="sep">|</span>Lead inspection<br>
    Radon inspection<span class="sep">|</span>Termite Inspection<span class="sep">|</span>Infared Scan
  </p>

  <p class="property-types">
    We provide inspections for single family homes condos co-ops town-homes<br>
    and Commercial property.
  </p>
</section>

</body>
</html>
```